Website Design Requirements

Domain Name: HometownTradesfolkRegistry.com

Website Look: Simple, Clean, Modern, and Professional Awarding Winning Website. Our Platform is the Best Directory Platform, all we need is a very creative person to make the following designs and select the fonts, font sizing, font colors and all the colors for the color points. We will follow up with the winner of the contest to design the rest of our design needs. The highlight of our brand is our Mascot; we feel this is something everyone will remember. It may be the easiest to obtain a free trial of the platform from Vantory Listings to complete this project. When we pick a winner of this contest we will provide the password to our admin panel for everything to be applied. Our Competitors are Perrows Hub, Yardwise Pro and Gravelnook.

We are thinking a light gray scale shadowing or graduated ghosting for the background behind the image of the Mascot for the main image. We want the Mascot and the Selection box to stand out as well as the logo.

Design Elements:
Main Page Image-Size for website is 1800 X 600px should be the Mascot on the right half of the image; this is where creative design is the most important. Design can use the head only from the waist up or the full image

Logo- Size for website is 450 X 70px; the logo should have the head of the mascot on a 3D icon with 2 line of text to the right side. The top line should have Hometown Tradesfolk the second line should have the word Directory in smaller size and be ghosted. The main idea about the logo is the icon and the words Hometown Tradesfolk. Note example can be seen on the Vantory Listings Rapid Launch Walkthrough on Clip Vue.

Favicon- Size for website is 56 X 56px should be the head of the mascot the Favicon and Google Map Pin drop could be the same if design is nice enough

Google Map Pin Drop- 25 X 46px should be the head of the mascot with a arrow pointing down.

Member Badge Image- Size 250 X 250px should be the head of the mascot inside a round ring with the words Verified –Certified –Member.

Target Market(s)

Consumers will use this website to locate Contractors in their Local area. Contractors will list their business on this website for a fee.

Industry/Entity Type

Domain

Contact Information for Business Card

Marcus Oldfield
Partner
555.014.2871
Marcus@HometownTradesfolkRegistry.Com
WWW. HometownTradesfolkRegistry.com

Logo Text

Hometown Tradesfolk Registry

Number of Pages Required

3 page

Font styles to use
Serif

Colors
ec1f27
fbed22

Requirements
Must have
• The use of our mascot, you can use full body view, waist up or head shot
Nice to have
• Clean bright colored Mascot, listing on back of card
• Hometown Tradesfolk
• Electricians
• Plumbers
• HVAC
• Landscapers
• General Contractors
• Garage Door Repair
• Carpet Cleaners
• Concrete Contractors

```html
<!DOCTYPE html>
<html lang="en">
<head>
<meta charset="utf-8">
<title>Hometown Tradesfolk Registry</title>
<link rel="stylesheet" href="https://fonts.googleapis.com/css2?family=Tinos:wght@400;700&display=swap">
<style>
  :root {
    --header-grey: #f0f0f0;
    --brand-blue: #2277d6;
    --brand-red: #ec1f27;
    --brand-yellow: #fbed22;
    --ink-blue: #2a6fc0;
    --white: #ffffff;
    --field-fill: #e6edf6;
    --field-line: #7ea3cf;
    --water-deep: #0d5f8c;
    --water-light: #9fd2ea;
    --figure-tone: #c9474c;
    --figure-tone-soft: #d86a6e;
  }
  * { box-sizing: border-box; margin: 0; padding: 0; }
  html, body { width: 1200px; height: 1008px; overflow: hidden; }
  body { font-family: "Tinos", "Times New Roman", serif; background: var(--white); }
  .page { position: relative; width: 1200px; height: 1008px; overflow: hidden; }

  /* Header */
  .site-header { position: absolute; left: 0; top: 0; width: 1200px; height: 104px; background: var(--header-grey); }
  .brand { position: absolute; left: 26px; top: 18px; display: flex; align-items: center; gap: 14px; }
  .brand-mark { width: 62px; height: 62px; border-radius: 50%; background: var(--brand-red); }
  .brand-name { font-size: 30px; color: var(--brand-red); letter-spacing: 0.5px; white-space: nowrap; }

  .member-login { position: absolute; left: 862px; top: 32px; width: 287px; }
  .member-login h2 { font-weight: 400; font-size: 13px; color: var(--ink-blue); text-align: center; letter-spacing: 0.5px; }
  .login-fields { display: flex; justify-content: space-between; margin-top: 10px; }
  .login-field { width: 138px; }
  .login-field span { display: block; font-size: 5px; color: var(--ink-blue); text-align: center; margin-bottom: 3px; letter-spacing: 0.4px; }
  .login-field i { display: block; height: 19px; background: var(--field-fill); border: 1px solid var(--field-line); border-radius: 2px; }

  /* Navigation */
  .main-nav { position: absolute; left: 0; top: 104px; width: 1200px; height: 59px; background: var(--brand-blue); }
  .nav-link { position: absolute; top: 23px; font-size: 11px; color: var(--white); padding-right: 6px; border-right: 1px solid var(--white); line-height: 13px; white-space: nowrap; }
  .site-search { position: absolute; left: 1020px; top: 12px; width: 175px; height: 32px; background: var(--white); border: 1px solid var(--field-line); }
  .site-search span { position: absolute; left: 8px; top: 10px; font-size: 9px; color: #555; }
  .site-search svg { position: absolute; right: 9px; top: 9px; }

  /* Hero */
  .hero { position: absolute; left: 0; top: 163px; width: 1200px; height: 262px; background: var(--brand-red); }
  .mascot-badge { position: absolute; left: 72px; top: 10px; width: 242px; height: 242px; border-radius: 50%; background: var(--white); }
  .mascot-badge-art { position: absolute; left: 26px; top: 26px; width: 190px; height: 190px; border-radius: 50%;
    background: linear-gradient(160deg, #f8d54a 0%, #f0b978 100%); }
  .finder { position: absolute; left: 761px; top: 64px; width: 360px; }
  .finder h1 { font-weight: 400; font-size: 31px; line-height: 36px; color: var(--white); letter-spacing: 0.5px; white-space: nowrap; }
  .finder-row { display: flex; justify-content: flex-end; align-items: center; gap: 6px; margin-top: 37px; width: 290px; }
  .finder-row + .finder-row { margin-top: 11px; }
  .finder-row span { font-size: 6px; color: var(--white); letter-spacing: 0.3px; white-space: nowrap; }
  .finder-row i { display: block; width: 136px; height: 19px; background: var(--white); border: 1px solid #d9d9d9; }

  /* Listings */
  .listings { position: absolute; left: 0; top: 425px; width: 1200px; height: 516px; }
  .listings-photo { position: absolute; inset: 0;
    background: linear-gradient(90deg, var(--water-deep) 0%, #1a7eb0 35%, #4aa6cf 62%, var(--water-light) 80%, #6bb6d8 100%); }
  .trade-list { position: absolute; list-style: none; color: var(--white); font-size: 15px; line-height: 18px; white-space: nowrap; }
  .mascot-figure { position: absolute; left: 860px; top: -17px; width: 224px; height: 533px; border-radius: 24px;
    background: linear-gradient(180deg, var(--figure-tone-soft) 0%, var(--figure-tone) 100%); }

  /* Footer */
  .site-footer { position: absolute; left: 0; top: 941px; width: 1200px; height: 67px; background: var(--brand-blue); }
  .footer-link { position: absolute; top: 28px; font-size: 8px; color: var(--white); padding-right: 5px; border-right: 1px solid var(--white); line-height: 10px; white-space: nowrap; }
  .social-links { position: absolute; left: 1092px; top: 28px; display: flex; gap: 6px; }
  .social-links i { display: block; width: 11px; height: 11px; background: var(--brand-red); }
</style>
</head>
<body>
<div class="page">

  <header class="site-header">
    <div class="brand">
      <span class="brand-mark"></span>
      <span class="brand-name">Hometown Tradesfolk</span>
    </div>
    <div class="member-login">
      <h2>MEMBER LOGIN</h2>
      <div class="login-fields">
        <div class="login-field"><span>USERNAME</span><i></i></div>
        <div class="login-field"><span>PASSWORD</span><i></i></div>
      </div>
    </div>
  </header>

  <nav class="main-nav">
    <span class="nav-link" style="left:87px">HOME</span>
    <span class="nav-link" style="left:282px">HOW IT WORKS</span>
    <span class="nav-link" style="left:531px">CONTACT US</span>
    <span class="nav-link" style="left:741px">LIST YOUR COMPANY</span>
    <div class="site-search">
      <span>SEARCH...</span>
      <svg width="14" height="14" viewBox="0 0 14 14" aria-hidden="true">
        <circle cx="5.5" cy="5.5" r="4" fill="none" stroke="#2277d6" stroke-width="2"/>
        <line x1="8.5" y1="8.5" x2="13" y2="13" stroke="#2277d6" stroke-width="2.2"/>
      </svg>
    </div>
  </nav>

  <section class="hero">
    <div class="mascot-badge">
      <div class="mascot-badge-art" role="img" aria-label="Mascot head: smiling tradesman in a yellow hard hat"></div>
    </div>
    <div class="finder">
      <h1>WHAT DO YOU NEED?</h1>
      <div class="finder-row"><span>ENTER KEYWORD</span><i></i></div>
      <div class="finder-row"><span>ENTER CITY OR ZIP CODE</span><i></i></div>
    </div>
  </section>

  <section class="listings">
    <div class="listings-photo" role="img" aria-label="Photo of a running water tap with splashing water in blue tones"></div>

    <ul class="trade-list" style="left:101px;top:66px">
      <li>HOMETOWN TRADESFOLK</li>
      <li>- ELECTRICIANS</li><li>- PLUMBERS</li><li>- HVAC</li><li>- LANDSCAPERS</li>
      <li>- GENERAL CONTRACTORS</li><li>- GARAGE DOOR REPAIR</li><li>- CARPET CLEANERS</li><li>- CONCRETE CONTRACTORS</li>
    </ul>
    <ul class="trade-list" style="left:459px;top:66px">
      <li>HOMETOWN TRADESFOLK</li>
      <li>- ELECTRICIANS</li><li>- PLUMBERS</li><li>- HVAC</li><li>- LANDSCAPERS</li>
      <li>- GENERAL CONTRACTORS</li><li>- GARAGE DOOR REPAIR</li><li>- CARPET CLEANERS</li><li>- CONCRETE CONTRACTORS</li>
    </ul>
    <ul class="trade-list" style="left:106px;top:281px">
      <li>HOMETOWN TRADESFOLK</li>
      <li>- ELECTRICIANS</li><li>- PLUMBERS</li><li>- HVAC</li><li>- LANDSCAPERS</li>
      <li>- GENERAL CONTRACTORS</li><li>- GARAGE DOOR REPAIR</li><li>- CARPET CLEANERS</li><li>- CONCRETE CONTRACTORS</li>
    </ul>
    <ul class="trade-list" style="left:464px;top:281px">
      <li>HOMETOWN TRADESFOLK</li>
      <li>- ELECTRICIANS</li><li>- PLUMBERS</li><li>- HVAC</li><li>- LANDSCAPERS</li>
      <li>- GENERAL CONTRACTORS</li><li>- GARAGE DOOR REPAIR</li><li>- CARPET CLEANERS</li><li>- CONCRETE CONTRACTORS</li>
    </ul>

    <div class="mascot-figure" role="img" aria-label="Full-body mascot: tradesman in hard hat, work shirt, jeans and tool belt, arms crossed"></div>
  </section>

  <footer class="site-footer">
    <span class="footer-link" style="left:34px">ABOUT US</span>
    <span class="footer-link" style="left:171px">PRIVACY</span>
    <span class="footer-link" style="left:272px">TERMS AND CONDITIONS</span>
    <div class="social-links" aria-label="Social links"><i></i><i></i><i></i><i></i></div>
  </footer>

</div>
</body>
</html>
```